Handover Document for post installation solar customers

I require a handover document (small A4 book) design for when we complete solar installations for our customers. It will need to have a brief description of next steps off the application process after installation aswell as some maintenance scheduling etc. This information will be provided by us.

Target Market(s)

Post installation customers (Solar)

Industry/Entity Type

Solar/ renewable

Colors
0054AA
0677BA
7BADD7
CADEEF
E8F1F8

Requirements
Must have
• Handover document provided in attatchment (must be made generic and not include customers details etc.) the attachment is only for reference. An intro "Thanks for using ZOV electrics.........". What happens next section
Nice to have
• Please use some of our past customers logos in our website - www.zovelectrics.com.au
Should not have
• Must be simple and look professional

```html
<!DOCTYPE html>
<html lang="en">
<head>
<meta charset="utf-8">
<title>ZOV Electrics – Solar System Owner's Manual</title>
<link href="https://fonts.googleapis.com/css2?family=Fira+Sans:wght@300;400;600;700&display=swap" rel="stylesheet">
<style>
:root{
  --bg:#eaeceb;
  --blue:#0e75bb;
  --blue-dark:#1a67a3;
  --text-blue:#0677ba;
  --ink:#444;
  --box:#333;
  --white:#fff;
}
*{margin:0;padding:0;box-sizing:border-box}
html,body{width:1200px;height:1200px;overflow:hidden;background:var(--bg);font-family:"Fira Sans",sans-serif}
.spread{position:absolute;left:120px;top:261px;width:960px;height:678px;background:var(--white);overflow:hidden}
.page{position:absolute;top:0;height:678px;width:480px}
.page-left{left:0}
.page-right{left:480px;background:linear-gradient(90deg,#d4d4d4 0%,#ececec 45%,#fff 60%)}
.header{position:absolute;top:0;left:0;width:480px;height:64px;background:var(--blue)}
.page-right .header{background:linear-gradient(90deg,var(--blue-dark),var(--blue) 60%)}
.brand{position:absolute;left:32px;top:20px;color:var(--white);font-weight:700;font-size:20px;letter-spacing:1px;display:flex;align-items:center;gap:8px}
.brand-mark{width:14px;height:14px;background:var(--white)}
.doc-title{position:absolute;right:32px;top:14px;text-align:right;color:var(--white);font-weight:700;font-size:16.5px;line-height:17.5px}
.section-head{position:absolute;top:81px;display:flex;align-items:center;gap:8px}
.section-num{width:35px;height:35px;background:var(--box);color:var(--white);font-weight:700;font-size:17px;display:flex;align-items:center;justify-content:center}
.section-title{font-size:15.5px;font-weight:400;color:#333}
.col{position:absolute;width:200px}
.subhead{font-size:10.5px;font-weight:400;color:var(--text-blue);border-bottom:1px solid var(--text-blue);padding-bottom:2px;margin-bottom:9px}
.body{font-size:9px;line-height:11.3px;letter-spacing:-0.1px;color:var(--ink);font-weight:300;text-align:justify}
.body p{margin-bottom:11.3px}
.lead{color:var(--text-blue);font-weight:400}
.bullets{list-style:none}
.bullets li{position:relative;padding-left:15px}
.bullets li::before{content:"•";position:absolute;left:0}
.warning{position:absolute;left:32px;width:200px;text-align:center;font-size:7px;line-height:9px;font-weight:400;color:#333}
.warning svg{display:block;margin:0 auto 3px}
.photo{position:absolute;left:0;top:484px;width:480px;height:194px;background:linear-gradient(180deg,#c9dbe9 0%,#8a9a7a 35%,#5f6f55 55%,#4b525c 75%,#6d737a 100%)}
.footer-line{position:absolute;top:628px;height:3px}
.page-left .footer-line{left:76px;width:404px;background:var(--blue)}
.page-right .footer-line{left:0;width:403px;background:var(--white)}
.page-num{position:absolute;top:598px;width:56px;height:64px}
.page-num span{position:absolute;inset:0;display:flex;align-items:center;justify-content:center;font-weight:700;font-size:17px}
.page-left .page-num{left:16px}
.page-left .page-num span{color:#333}
.page-right .page-num{left:408px}
.page-right .page-num span{color:var(--white)}
.footer-text{position:absolute;top:640px;font-size:8px;line-height:9.3px;font-weight:400}
.page-left .footer-text{right:32px;text-align:right;color:var(--text-blue)}
.page-right .footer-text{left:32px;color:#e8eef3}
.footer-text b{font-weight:600}
</style>
</head>
<body>
<div class="spread">
  <section class="page page-left">
    <header class="header">
      <div class="brand"><span class="brand-mark"></span>ZOV ELECTRICS</div>
    </header>
    <div class="section-head" style="left:32px"><div class="section-num">2</div><h2 class="section-title">Contact Information</h2></div>
    <div class="col" style="left:32px;top:133px">
      <h3 class="subhead">2.1 Installation Company</h3>
      <div class="body">
        <p>Lorem ipsum dolor sit amet, consectetur adipiscing elit. Nulla tincidunt felis eros, ut finibus ligula pulvinar sed. Maecenas at tellus vel lectus ullamcorper fringilla eget viverra diam. Nulla odio sem, fringilla a posuere nec, venenatis eget eros. Pellentesque quis sapien posuere, feugiat odio vel, hendrerit risus. In maximus lobortis nulla sit amet fringilla. Pellentesque aliquam laoreet sapien et mattis. Sed quis urna vehicula, laoreet lorem vitae, malesuada quam.</p>
        <p>Integer purus quam, consequat vel euismod ac, vestibulum ut dui. Cras non vehicula mauris, et auctor ligula. Morbi quis tempor risus. Nullam id bibendum est, id mollis ante. Phasellus maximus id nisi sed tempus. Pellentesque interdum placerat fermentum. Nunc lacinia nunc quis urna venenatis, ac ullamcorper ex fringilla.</p>
        <p>Quisque imperdiet aliquet ex, at pretium dolor ullamcorper at. Praesent gravida quam nec tortor iaculis, ac blandit orci semper. Aliquam non rhoncus tellus. Duis laoreet metus nec iaculis rutrum. Fusce eu libero sodales, rhoncus eros eu, lobortis ipsum. Nam elementum, nisi vel tincidunt sagittis, augue ex ultricies justo, a tempor augue nulla auctor tortor. Vestibulum sed finibus dolor. Curabitur a nisl laoreet odio auctor rhoncus ut ullamcorper nibh. Aenean ut orci velit. Aliquam erat volutpat. Aenean ultrices dui ac viverra eleifend. Maecenas blandit laoreet nisl vel tristique. Ut rhoncus, odio mollis fringilla gravida, dolor ligula congue sapien, id congue lorem magna ac massa. Vivamus viverra, est at dapibus porta, metus nibh sagittis felis, sit amet ullamcorper augue lacus vel neque.</p>
      </div>
    </div>
    <div class="col" style="left:248px;top:133px">
      <h3 class="subhead">2.2 Accredited Installer</h3>
      <div class="body">
        <p>Lorem ipsum dolor sit amet, consectetur adipiscing elit. Nulla tincidunt felis eros, ut finibus ligula pulvinar sed. Maecenas at tellus vel lectus ullamcorper fringilla eget viverra diam. Nulla odio sem, fringilla a posuere nec, venenatis eget eros. Pellentesque quis sapien posuere, feugiat odio vel, hendrerit risus. In maximus lobortis nulla sit amet fringilla. Pellentesque aliquam laoreet sapien et mattis. Sed quis urna vehicula, laoreet lorem vitae, malesuada quam.</p>
        <p>Integer purus quam, consequat vel euismod ac, vestibulum ut dui. Cras non vehicula mauris, et auctor ligula. Morbi quis tempor risus. Nullam id bibendum est, id mollis ante. Phasellus maximus id nisi sed tempus. Pellentesque interdum placerat fermentum. Nunc lacinia nunc quis urna venenatis, ac ullamcorper ex fringilla.</p>
        <p>Quisque imperdiet aliquet ex, at pretium dolor ullamcorper at. Praesent gravida quam nec tortor iaculis, ac blandit orci semper. Aliquam non rhoncus tellus. Duis laoreet metus nec iaculis rutrum. Fusce eu libero sodales, rhoncus eros eu, lobortis ipsum. Nam elementum, nisi vel tincidunt sagittis, augue ex ultricies justo, a tempor augue nulla auctor tortor. Vestibulum sed finibus dolor. Curabitur a nisl laoreet odio auctor rhoncus ut ullamcorper nibh. Aenean ut orci velit. Aliquam erat volutpat. Aenean ultrices dui ac viverra eleifend. Maecenas blandit laoreet nisl vel tristique. Ut rhoncus, odio mollis fringilla gravida, dolor ligula congue sapien, id congue lorem magna ac massa. Vivamus viverra, est at dapibus porta, metus nibh sagittis felis, sit amet ullamcorper augue lacus vel neque.</p>
      </div>
    </div>
    <div class="footer-line"></div>
    <div class="page-num">
      <svg width="56" height="64" viewBox="0 0 56 64"><polygon points="28,3 53,17 53,47 28,61 3,47 3,17" fill="#fff" stroke="#0e75bb" stroke-width="4"/></svg>
      <span>02</span>
    </div>
    <div class="footer-text"><b>ZOV Electrics Pty Ltd</b><br>Suite 4, 88 Harbour Lane, Kestrel Bay Victoria 3999<br>(03) 5550 0142 | info@zovelectrics.com.au</div>
  </section>

  <section class="page page-right">
    <header class="header">
      <div class="doc-title">Solar System<br>Owner's Manual</div>
    </header>
    <div class="photo" role="img" aria-label="Photo of rooftop solar panels on a building overlooking trees and suburbs"></div>
    <div class="section-head" style="left:32px"><div class="section-num">3</div><h2 class="section-title">Precautions and Warnings</h2></div>
    <div class="col" style="left:32px;top:136px">
      <div class="body lead"><p style="margin-bottom:9px">Your solar power system is designed for automatic operations with no need for user interaction. It is safe when installed and operating correctly. However, given the D.C. and A.C. voltages present in the system, significant inherent danger still remain.<br>Please read and understand all safety instructions, warnings and cautions before using the system.</p></div>
      <h3 class="subhead">3.1 Warning Symbols</h3>
      <div class="body"><p>The following symbols will appear in this manual. They are used to indicate potentially hazardous situations where necessary precautions should be taken.</p></div>
    </div>
    <div class="warning" style="top:323px">
      <svg width="50" height="43" viewBox="0 0 50 43"><polygon points="25,2 48,41 2,41" fill="#e5b322" stroke="#111" stroke-width="3" stroke-linejoin="round"/><rect x="22.5" y="13" width="5" height="16" rx="2" fill="#111"/><circle cx="25" cy="34" r="2.8" fill="#111"/></svg>
      General Safety Warning:<br>Failure to follow recommended<br>procedure could result in injury
    </div>
    <div class="warning" style="top:410px">
      <svg width="50" height="43" viewBox="0 0 50 43"><polygon points="25,2 48,41 2,41" fill="#e5b322" stroke="#111" stroke-width="3" stroke-linejoin="round"/><polygon points="27,12 20,27 25,27 22,37 31,22 26,22 29,12" fill="#111"/></svg>
      General Safety Warning:<br>Failure to follow recommended<br>procedure could result in injury
    </div>
    <div class="col" style="left:248px;top:133px">
      <h3 class="subhead">3.2 Important Safety Information</h3>
      <ul class="body bullets">
        <li>Do not attempt to service your solar system unless you are a licensed electrician and your work is carried out in accordance with local and national electrical codes and standards.</li>
        <li>Any low voltage (LV) work must be undertaken by a suitably licensed electrical worker or contractor. LV is specified in the Australian Standards as any voltage equal to or higher than 50V AC or 120V DC.</li>
        <li>Do not touch any electric components, e.g. wires, connection terminals junction boxes or plug connectors.</li>
        <li>Do not open any components of your solar system unless adequately licensed to do so.</li>
        <li>We strongly advise against climbing onto the roof to clean or inspect solar panel modules. This should only done by professionals with appropriate training and safety equipment.</li>
        <li>Observe all safety signage and warnings associated with the system. Ensure these signs remain in place and visible.</li>
        <li>Familiarize yourself with the Shutdown Procedures and Earth Fault Alarm event actions. This involves understanding the relevant components and signage for these emergencies.</li>
        <li>In case of fire, shut down the system if safe to do so. Circuit breakers must remain off until the fire is extinguished.</li>
        <li>Note that a small, non-lethal electrical charge may exist at the base frame or module frames even when the system has been shut down. Inform all necessary roof workers before commencement of works.</li>
      </ul>
    </div>
    <div class="footer-line"></div>
    <div class="page-num">
      <svg width="56" height="64" viewBox="0 0 56 64"><polygon points="28,3 53,17 53,47 28,61 3,47 3,17" fill="none" stroke="#fff" stroke-width="4"/></svg>
      <span>03</span>
    </div>
    <div class="footer-text"><b>ZOV Electrics Pty Ltd</b><br>Suite 4, 88 Harbour Lane, Kestrel Bay Victoria 3999<br>(03) 5550 0142 | info@zovelectrics.com.au</div>
  </section>
</div>
</body>
</html>
```